Automotive component supplier needs a business card design

We need a business card design for our company called Velmar Global Components Ltd based in the UK. We are a supplier of interior and exterior components to premium car manufacturers such as Corvane Hale, Durrant Fyfe, Maxtorn and Valdessimo. We would like to see a modern business card design that uses the colour blue.

Target Market(s)

Premium automotive car manufacturers.

Industry/Entity Type

Automotive

Contact Information for Business Card

Company Name : Velmar Global Components Limited
Address: 17 Tamsey Yard, Upper Drisk, Warwick, CV31 8RJ, United Kingdom
Web Address : www.velmarparts-example.co.uk

Font styles to use
Other font styles liked:
• Helvetica

Colors
3176b5
0255a3
85acd3
cfdeed
cee9f5
85cae6
34a6d7
0692cd
9bcb3c

Requirements
Must have
• Clear company logo and a mixture of blue colours.
Nice to have
• A high quality modern image.
Should not have
• Multiple colours.

```html
<!DOCTYPE html>
<html lang="en">
<head>
<meta charset="utf-8">
<title>Velmar Global Components – Business Card</title>
<link rel="stylesheet" href="https://fonts.googleapis.com/css2?family=Arimo:wght@400;700&display=swap">
<style>
  :root {
    --bg: #2b2b2d;
    --blue-bright: #0692cd;
    --blue-mid: #34a6d7;
    --blue-light: #85cae6;
    --blue-deep: #0255a3;
    --blue-strip: #1a86c6;
    --green: #9bcb3c;
    --black: #050505;
    --white: #ffffff;
  }
  * { margin: 0; padding: 0; box-sizing: border-box; }
  html, body { width: 1200px; height: 900px; overflow: hidden; }
  body {
    background: var(--bg);
    font-family: "Arimo", Helvetica, Arial, sans-serif;
    position: relative;
  }
  .card {
    position: absolute;
    left: 250px;
    width: 700px;
    height: 400px;
    overflow: hidden;
    box-shadow: 0 10px 30px rgba(0,0,0,.45);
  }
  .card-front { top: 35px; background: var(--blue-mid); }
  .card-back { top: 465px; background: linear-gradient(135deg, var(--blue-bright), var(--blue-mid)); }

  .front-texture {
    position: absolute; inset: 0;
    background: linear-gradient(160deg, var(--blue-mid), var(--blue-bright));
  }
  .brand { position: absolute; line-height: 1; }
  .brand-row { display: flex; align-items: center; gap: 10px; }
  .brand-mark { width: 16px; height: 16px; background: var(--green); }
  .brand-name { font-weight: 700; font-size: 64px; letter-spacing: 1px; }
  .brand-tag { font-size: 14px; letter-spacing: 2.4px; margin-top: 4px; text-align: right; }
  .card-front .brand { right: 50px; bottom: 70px; color: var(--white); }
  .card-back .brand { left: 34px; top: 40px; color: var(--blue-bright); }
  .card-back .brand-tag { text-align: left; padding-left: 26px; }

  .card-shape { position: absolute; inset: 0; }

  .address {
    position: absolute;
    left: 34px; bottom: 125px;
    color: var(--blue-bright);
    font-size: 17px;
    font-style: normal;
    line-height: 1.3;
  }
  .contact {
    position: absolute;
    right: 32px; top: 128px;
    text-align: right;
    color: var(--white);
  }
  .contact-name { font-weight: 700; font-size: 21px; letter-spacing: 1.5px; }
  .contact-role { color: var(--green); font-size: 15px; margin-top: 2px; margin-bottom: 14px; }
  .contact-line {
    display: flex; justify-content: flex-end; align-items: center; gap: 9px;
    font-size: 15px; line-height: 1.5;
  }
  .contact-line svg { width: 12px; height: 12px; flex: none; }
</style>
</head>
<body>

<section class="card card-front" aria-label="Card front">
  <div class="front-texture" role="img" aria-label="Blue background with a subtle repeated brand pattern"></div>
  <div class="brand">
    <div class="brand-row">
      <span class="brand-mark"></span>
      <span class="brand-name">VELMAR</span>
    </div>
    <div class="brand-tag">GLOBAL COMPONENTS</div>
  </div>
</section>

<section class="card card-back" aria-label="Card back">
  <svg class="card-shape" viewBox="0 0 700 400" preserveAspectRatio="none" aria-hidden="true">
    <path d="M0 362 C160 384 290 330 380 250 C440 190 490 100 540 0 H0 Z" fill="var(--blue-strip)"/>
    <path d="M0 356 C158 378 285 324 374 245 C434 185 484 96 532 0" fill="none" stroke="var(--black)" stroke-width="5"/>
    <path d="M0 350 C155 372 280 318 368 240 C428 180 477 92 525 0 H0 Z" fill="var(--green)"/>
    <path d="M0 322 C150 342 265 295 350 222 C408 165 455 80 500 0 H0 Z" fill="var(--black)"/>
  </svg>

  <div class="brand">
    <div class="brand-row">
      <span class="brand-mark"></span>
      <span class="brand-name">VELMAR</span>
    </div>
    <div class="brand-tag">GLOBAL COMPONENTS</div>
  </div>

  <address class="address">
    17 Tamsey Yard, Upper Drisk<br>
    Warwick, CV31 8RJ, UK
  </address>

  <div class="contact">
    <div class="contact-name">ELWYN TARROW</div>
    <div class="contact-role">Director</div>
    <div class="contact-line">700 555-0142
      <svg viewBox="0 0 16 16"><path d="M3 1l3 3-2 2c1 2 3 4 5 5l2-2 3 3-2 3C7 15 1 9 1 3z" fill="var(--green)"/></svg>
    </div>
    <div class="contact-line">700 555-0187
      <svg viewBox="0 0 16 16"><rect x="4" y="1" width="8" height="14" rx="1.5" fill="none" stroke="var(--green)" stroke-width="1.6"/><circle cx="8" cy="12.5" r="1" fill="var(--green)"/></svg>
    </div>
    <div class="contact-line">hello@velmarparts-example.co.uk
      <svg viewBox="0 0 16 16"><rect x="1" y="3" width="14" height="10" fill="var(--green)"/><path d="M1 3l7 6 7-6" fill="none" stroke="#0692cd" stroke-width="1.2"/></svg>
    </div>
    <div class="contact-line">www.velmarparts-example.co.uk
      <svg viewBox="0 0 16 16"><circle cx="8" cy="8" r="6.5" fill="none" stroke="var(--green)" stroke-width="1.6"/><path d="M1.5 8h13M8 1.5c-3 3.5-3 9.5 0 13M8 1.5c3 3.5 3 9.5 0 13" fill="none" stroke="var(--green)" stroke-width="1.2"/></svg>
    </div>
  </div>
</section>

</body>
</html>
```